Corporate Hollowmere business cards to be handed to investor, bankers etc. Needs to have a young feel

I need business cards designed for a technology company that provides vanto-like rapid response on the security industry. I would like it simple but very cool and tasteful. See attached documents for artwork and colours to be used. Cut sheet describes business model. Card stock should be thicker than normal. I would like the one side to be just the art and the other to have the contact info with maybe the pin somewhere.

Target Market(s)

Investors

Industry/Entity Type

Business

Contact Information for Business Card

Would like the logo attached on one side with name address and other info on the other side.

Font styles to use
Other font styles liked:
• See existing logo

Colors
6b449b
886aae
e4daeb
ffffff

Requirements
Must have
• Name: Gregory Thalassides
• Address: 47 Orchard Lane, Toronto, On, L6R2C8
• Tel: 647-5550192
• Email: greg@hollowmere.io
Nice to have
• See logo colours

```html
<!DOCTYPE html>
<html lang="en">
<head>
<meta charset="utf-8">
<title>Hollowmere Business Cards</title>
<link rel="stylesheet" href="https://fonts.googleapis.com/css2?family=Questrial&display=swap">
<style>
  :root {
    --ink: #1a1a1a;
    --brand-purple: #7f5fa9;
    --brand-lilac: #f2eff7;
    --card: #ffffff;
    --backdrop: #f1f1f1;
    --card-edge: #e2e2e2;
  }
  * { margin: 0; padding: 0; box-sizing: border-box; }
  html, body {
    width: 1200px; height: 1200px; overflow: hidden;
    background: var(--backdrop);
    font-family: "Questrial", sans-serif;
  }
  .stage { position: relative; width: 1200px; height: 1200px; }
  .card {
    position: absolute; width: 680px; height: 388px;
    background: var(--card); overflow: hidden;
    border: 1px solid var(--card-edge);
  }
  .card--back { left: 391px; top: 564px; }
  .card--front { left: 151px; top: 230px; }

  .wordmark {
    display: flex; align-items: center; color: var(--ink);
    font-family: "Questrial", sans-serif; font-weight: 400; line-height: 1;
  }
  .wordmark__dot { border-radius: 50%; background: var(--brand-purple); flex: none; }

  .card--front .wordmark {
    position: absolute; left: 50%; top: 50%;
    transform: translate(-50%, -50%); font-size: 76px; letter-spacing: -1px;
  }
  .card--front .wordmark__dot { width: 38px; height: 38px; margin-right: 14px; margin-top: 10px; }

  .contact {
    position: absolute; left: 209px; top: 116px; transform: translateX(-50%);
    display: flex; flex-direction: column; align-items: center;
    white-space: nowrap; color: var(--ink);
  }
  .contact .wordmark { font-size: 25px; letter-spacing: -0.4px; margin-bottom: 14px; }
  .contact .wordmark__dot { width: 13px; height: 13px; margin-right: 4px; margin-top: 4px; }
  .contact__name { color: var(--brand-purple); font-size: 23px; margin-bottom: 10px; }
  .contact__line { font-size: 16px; line-height: 20px; display: flex; align-items: center; gap: 3px; }
  .contact__line svg { fill: var(--brand-purple); }

  .accent { position: absolute; border-radius: 50%; }
  .accent--halo { width: 432px; height: 432px; left: 353px; top: 64px; background: var(--brand-lilac); }
  .accent--core { width: 232px; height: 232px; left: 449px; top: 156px; background: var(--brand-purple); }
</style>
</head>
<body>
<main class="stage">
  <section class="card card--back" aria-label="Business card, contact side">
    <div class="accent accent--halo"></div>
    <div class="accent accent--core"></div>
    <div class="contact">
      <div class="wordmark"><span class="wordmark__dot"></span>hollowmere</div>
      <p class="contact__name">Gregory Thalassides</p>
      <p class="contact__line">47 Orchard Lane, Toronto, On, L6R2C8</p>
      <p class="contact__line">
        <svg width="11" height="12" viewBox="0 0 24 24" aria-hidden="true"><path d="M6.6 10.8a15.1 15.1 0 0 0 6.6 6.6l2.2-2.2a1 1 0 0 1 1-.25 11.4 11.4 0 0 0 3.6.6 1 1 0 0 1 1 1V20a1 1 0 0 1-1 1A17 17 0 0 1 3 4a1 1 0 0 1 1-1h3.5a1 1 0 0 1 1 1c0 1.25.2 2.45.6 3.6a1 1 0 0 1-.25 1z"/></svg>
        647-5550192
      </p>
      <p class="contact__line">
        <svg width="14" height="10" viewBox="0 0 24 16" aria-hidden="true"><path d="M1 0h22a1 1 0 0 1 1 1v14a1 1 0 0 1-1 1H1a1 1 0 0 1-1-1V1a1 1 0 0 1 1-1zm1 3v11h20V3l-10 6zm1.5-1L12 7l8.5-5z"/></svg>
        greg@hollowmere.io
      </p>
    </div>
  </section>

  <section class="card card--front" aria-label="Business card, logo side">
    <div class="wordmark"><span class="wordmark__dot"></span>hollowmere</div>
  </section>
</main>
</body>
</html>
```